Redesign of 3-4 page site for professional services firm

Our site is www.kestrelvaleadvisors.com. We currently have a simple page made with HostNimbo tools. But the tools are not able to generate the look and feel we desire. We need a home page similar to current that tells a little about our company, our experience and our team. We need a second page to show details of current and past transactions we have assisted our clients with. Currently this page reads like a word document but we would like for it to present in a cleaner fashion and liven it up with some images that link to the industry served. For example, a motorcycle outline in a circle for the powersports related transactions. We would like page to introduce each member of "Our Team" and highlight their experience with a photo of each person. If there is no photo available, we would like a placeholder to be their initials in a circle that can be updated later. We would also like a contact us section whether this is a different page or part of the home page.

Target Market(s)

Retirement minded business owners

Industry/Entity Type

Professional Services

Coding

Coded - Design and coding required

Requirements
Must have
• See project description. Must include a page or section for "Current Listings" and "Recently Completed Transactions" (can be same page)

```html
<!DOCTYPE html>
<html lang="en">
<head>
<meta charset="utf-8">
<title>Kestrel Vale Business Brokers</title>
<link href="https://fonts.googleapis.com/css2?family=Open+Sans:wght@400;600;700;800&display=swap" rel="stylesheet">
<style>
:root{
  --green:#1f9a1f;
  --green-dark:#137a13;
  --ink:#1c1c1c;
  --text:#333;
  --grey:#f0f0f0;
  --panel:#e6e6e6;
  --footer:#1e1e1e;
  --white:#fff;
}
*{box-sizing:border-box;margin:0;padding:0}
html,body{width:1200px;height:4168px;overflow:hidden}
body{font-family:"Open Sans",Arial,sans-serif;color:var(--text);background:var(--white);position:relative}
.btn{display:inline-block;background:var(--green);color:#fff;font-weight:700;font-size:15px;padding:12px 22px;border-radius:3px;text-transform:uppercase;white-space:nowrap}
.btn-outline{display:inline-block;background:#fff;color:var(--ink);font-weight:700;font-size:15px;padding:12px 22px;border-radius:24px;text-transform:uppercase;white-space:nowrap}
.photo{position:absolute}

/* header */
.site-header{position:absolute;top:0;left:0;width:1200px;height:90px;display:flex;align-items:center;justify-content:space-between;padding:0 100px 0 110px;z-index:3}
.brand{font-size:26px;font-weight:700;color:var(--ink);display:flex;align-items:center;gap:10px}
.brand-dot{width:18px;height:18px;background:var(--green);border-radius:50%}
.nav{display:flex;gap:30px;align-items:center;font-size:15px;font-weight:700;color:var(--ink);text-transform:uppercase}
.nav .active{color:var(--green);border-bottom:2px solid var(--green)}
.nav .btn{font-size:14px;padding:10px 16px}

/* hero */
.hero{position:absolute;top:0;left:0;width:1200px;height:700px}
.hero-photo{left:500px;top:0;width:700px;height:600px;background:linear-gradient(135deg,#d9dde3,#8f9aa6 60%,#3f4852)}
.hero-copy{position:absolute;left:110px;top:195px}
.hero-copy .kicker{font-size:15px;font-weight:600;color:var(--ink);margin-bottom:12px}
.hero-copy h1{font-size:42px;line-height:1.2;font-weight:400;color:var(--ink)}
.hero-copy h1 strong{font-weight:800;text-transform:uppercase}
.hero-copy h1 .hl{color:var(--green)}
.hero-copy .sub{font-size:20px;font-weight:600;color:var(--ink);margin:18px 0 42px}
.hero-curve{position:absolute;left:0;top:520px}

/* section titles */
.section-title{position:absolute;left:0;width:1200px;text-align:center;font-size:44px;font-weight:400;color:var(--ink);text-transform:uppercase}
.section-title strong{color:var(--green);font-weight:800}
.lead{position:absolute;left:160px;width:880px;text-align:center;font-size:15px;line-height:1.6;color:var(--text)}

.about-photo{left:0;top:905px;width:1200px;height:430px;background:linear-gradient(120deg,#c9cfd6,#a6abb2 45%,#7c858e)}

/* experience */
.experience{position:absolute;left:0;top:1335px;width:1200px;height:490px;background:var(--green);color:#fff}
.experience h2{position:absolute;left:110px;top:72px;font-size:44px;font-weight:400}
.experience h2 strong{font-weight:800;text-transform:uppercase}
.experience .copy{position:absolute;left:110px;top:160px;width:640px;font-size:15px;line-height:1.55}
.experience .copy p{margin-bottom:16px}
.exp-photo{left:790px;top:1405px;width:330px;height:330px;background:linear-gradient(160deg,#9ea7b2,#3a4450)}

/* team */
.team-grid{position:absolute;left:112px;top:2280px;width:976px;display:grid;grid-template-columns:repeat(4,244px);grid-template-rows:repeat(2,205px)}
.member-photo{background:linear-gradient(180deg,#dfe3e7,#8d96a0)}
.member-bio{background:var(--panel);padding:18px 16px;font-size:12px;line-height:1.45;color:var(--text)}
.member-bio.featured{background:var(--green);color:#fff}
.member-bio h3{font-size:14px;font-weight:700;text-transform:uppercase;margin-bottom:8px;color:inherit}
.member-bio .more{display:block;margin-top:10px;font-weight:700;font-size:12px}

/* listings */
.tabs{position:absolute;left:310px;top:2880px;width:580px;height:60px;border-radius:30px;background:var(--grey);box-shadow:0 2px 6px rgba(0,0,0,.2);display:flex}
.tab{display:flex;align-items:center;justify-content:center;font-size:17px;color:var(--ink);white-space:nowrap}
.tab.active{width:320px;background:var(--green);color:#fff;border-radius:30px}
.tab.rest{flex:1}
.listings{position:absolute;left:140px;top:2990px;width:920px;display:flex;justify-content:space-between}
.listing{width:200px;text-align:center}
.listing-icon{width:100px;height:100px;margin:0 auto 20px;border-radius:6px;background:var(--green)}
.listing h4{font-size:19px;font-weight:600;color:var(--ink);line-height:1.3}

/* contact */
.contact{position:absolute;left:0;top:3260px;width:1200px;height:580px;background:var(--green);color:#fff}
.contact h2{position:absolute;left:110px;top:60px;font-size:44px;font-weight:800;text-transform:uppercase}
.contact p{position:absolute;left:110px;top:140px;width:470px;font-size:15px;line-height:1.55}
.contact .btn-outline{position:absolute;left:110px;top:268px;font-size:14px}
.contact-photo{left:640px;top:3260px;width:560px;height:470px;background:linear-gradient(140deg,#e7ebef,#9aa4ae)}
.contact-card{position:absolute;left:150px;top:3620px;width:320px;height:200px;background:#fff;box-shadow:0 4px 14px rgba(0,0,0,.25);padding:28px 26px;font-size:14px;color:var(--ink);z-index:2}
.contact-card h3{font-size:17px;font-weight:700;margin-bottom:18px;white-space:nowrap}
.contact-card .row{display:flex;gap:12px;align-items:flex-start;margin-bottom:14px;line-height:1.4}
.map{left:490px;top:3640px;width:360px;height:240px;background:linear-gradient(135deg,#eef0ea,#d7dccf);border:1px solid #ccc;z-index:2}

/* footer */
.site-footer{position:absolute;left:0;top:3840px;width:1200px;height:288px;background:var(--footer);color:#ddd}
.footer-about{position:absolute;left:110px;top:100px;width:300px;font-size:14px;line-height:1.5}
.footer-about h4{color:var(--green);font-size:16px;font-weight:700;margin-bottom:10px}
.footer-brand{position:absolute;left:490px;top:140px;font-size:26px;font-weight:700;color:#fff;white-space:nowrap}
.footer-nav{position:absolute;left:750px;top:180px;display:flex;gap:24px;font-size:13px;font-weight:700;text-transform:uppercase;color:#fff}
.footer-nav .active{color:var(--green);border-bottom:2px solid var(--green)}
.social{position:absolute;left:900px;top:120px;display:flex;gap:10px}
.social span{width:24px;height:24px;border-radius:50%;background:#fff;display:block}
.copyright{position:absolute;left:0;top:4128px;width:1200px;height:40px;background:#111;color:#bbb;font-size:12px;display:flex;align-items:center;justify-content:center}
</style>
</head>
<body>

<header class="site-header">
  <div class="brand"><span class="brand-dot"></span>Kestrel Vale</div>
  <nav class="nav">
    <span class="active">Home</span><span>About Us</span><span>Our Team</span><span>Current Listings</span><span class="btn">Get In Touch</span>
  </nav>
</header>

<section class="hero">
  <div class="photo hero-photo" role="img" aria-label="Business team in suits discussing a deal in a bright office"></div>
  <svg class="hero-curve" width="1200" height="180" viewBox="0 0 1200 180" aria-hidden="true">
    <path d="M0 120 C400 40 800 40 1200 60 L1200 180 L0 180 Z" fill="#fff"/>
    <path d="M0 120 C400 40 800 40 1200 60" fill="none" stroke="#1f9a1f" stroke-width="14"/>
  </svg>
  <div class="hero-copy">
    <div class="kicker">WELCOME</div>
    <h1>Strategically<br><strong>Navigating <span class="hl">Business</span><br>Exits</strong></h1>
    <div class="sub">GET STARTED TODAY</div>
    <span class="btn">Contact Us</span>
  </div>
</section>

<h2 class="section-title" style="top:680px">About Our <strong>Company</strong></h2>
<p class="lead" style="top:750px">At Kestrel Vale Business Brokers, our mission is to empower entrepreneurs and business owners by facilitating seamless transactions that lead to mutual success. We understand that selling or acquiring a business can be a complex and emotional journey, which is why our dedicated team of experts is here to guide you every step of the way. With a commitment to integrity, transparency, and unmatched professionalism, we strive to create a positive and rewarding experience for all our clients.</p>

<div class="photo about-photo" role="img" aria-label="Colleagues smiling around a meeting table with laptops"></div>

<section class="experience">
  <h2>Our <strong>Experience</strong></h2>
  <div class="copy">
    <p>With decades of experience Kestrel Vale Business Brokers has proudly assisted numerous clients in successfully navigating the intricate journey of selling their businesses.</p>
    <p>Our team brings a wealth of knowledge and expertise acquired through years of working closely with entrepreneurs and business owners across diverse industries. We understand the unique challenges and complexities involved in selling a business, from valuation and marketing to negotiations and closing the deal.</p>
    <p>Our extensive experience allows us to anticipate potential obstacles and proactively find solutions, ensuring a seamless and efficient process for our clients. We take pride in our track record of delivering exceptional results and helping our clients achieve their desired outcomes.</p>
  </div>
</section>
<div class="photo exp-photo" role="img" aria-label="Group of professionals standing together in business attire"></div>

<h2 class="section-title" style="top:2060px">Our Team</h2>
<p class="lead" style="top:2150px">Together, our team of CPAs, attorneys, real estate brokers, and financial advisors work collaboratively to provide you with a holistic approach to business transactions. With our combined knowledge and experience, we strive to ensure a smooth and successful journey for our clients, delivering exceptional results and peace of mind.</p>

<div class="team-grid">
  <div class="member-photo" role="img" aria-label="Portrait of Marcus Hale"></div>
  <div class="member-bio featured"><h3>Marcus Hale, CPA, JD</h3>Marcus is a licensed broker, Certified Public Accountant and attorney. His blend of tax, legal and financial insight helps owners prepare, value and close their sale with confidence.<span class="more">Read More ›</span></div>
  <div class="member-photo" role="img" aria-label="Portrait of Owen Pritchard"></div>
  <div class="member-bio"><h3>Owen Pritchard</h3>Owen is a seasoned professional with 30+ years of experience as a licensed broker and executive. He has guided many owners through the sale of family and closely held firms.<span class="more">Read More ›</span></div>
  <div class="member-bio"><h3>Luke Danner</h3>Luke has more than 20 years of experience within the financial and insurance services fields. He has helped owners plan ahead, protect value and prepare for a smooth transition.<span class="more">Read More ›</span></div>
  <div class="member-photo" role="img" aria-label="Portrait of Luke Danner"></div>
  <div class="member-bio"><h3>Reid Callow</h3>Reid is a sales and marketing expert in the powersports and automotive industries with a track record of growing dealerships from small starts into leading regional businesses.<span class="more">Read More ›</span></div>
  <div class="member-photo" role="img" aria-label="Portrait of Reid Callow"></div>
</div>

<h2 class="section-title" style="top:2780px">Business Listings</h2>
<div class="tabs"><div class="tab active">Recently Completed Business Sales</div><div class="tab rest">Current Business Listings</div></div>
<div class="listings">
  <div class="listing"><div class="listing-icon" role="img" aria-label="Sports venue icon"></div><h4>Sports and Entertainment Venue</h4></div>
  <div class="listing"><div class="listing-icon" role="img" aria-label="Motorcycle icon"></div><h4>Powersports Dealership</h4></div>
  <div class="listing"><div class="listing-icon" role="img" aria-label="Tax document icon"></div><h4>Bookkeeping and Tax Practice</h4></div>
  <div class="listing"><div class="listing-icon" role="img" aria-label="Excavator icon"></div><h4>Dirt Work and Excavating</h4></div>
</div>

<section class="contact">
  <h2>Contact Us</h2>
  <p>We strive to stay in communication with our clients. Have a question about how we can match your specific needs? Send us a message, or give us a call. We're always happy to meet new customers!</p>
  <span class="btn-outline">Get Started Today ›</span>
</section>
<div class="photo contact-photo" role="img" aria-label="Support staff with headsets working at computers"></div>

<div class="contact-card">
  <h3>Kestrel Vale Business Brokers</h3>
  <div class="row">
    <svg width="18" height="22" viewBox="0 0 18 22" aria-hidden="true"><path d="M9 0C4 0 0 4 0 9c0 6 9 13 9 13s9-7 9-13c0-5-4-9-9-9z" fill="#1f9a1f"/><circle cx="9" cy="9" r="3.5" fill="#fff"/></svg>
    <span>820 Harlow Street, Brookfield, Oklahoma 74100, United States</span>
  </div>
  <div class="row">
    <svg width="18" height="18" viewBox="0 0 24 24" aria-hidden="true"><path d="M6.6 10.8a15 15 0 0 0 6.6 6.6l2.2-2.2a1 1 0 0 1 1-.25 11.4 11.4 0 0 0 3.6.6 1 1 0 0 1 1 1V20a1 1 0 0 1-1 1A17 17 0 0 1 3 4a1 1 0 0 1 1-1h3.5a1 1 0 0 1 1 1c0 1.25.2 2.45.6 3.6a1 1 0 0 1-.25 1z" fill="#1f9a1f"/></svg>
    <span>405-555-0147</span>
  </div>
</div>
<div class="photo map" role="img" aria-label="Map showing the office location"></div>

<footer class="site-footer">
  <div class="footer-about"><h4>ABOUT</h4>Kestrel Vale Business Brokers is a boutique business advisory firm helping entrepreneurs sell, grow, or transition their businesses.</div>
  <div class="footer-brand">Kestrel Vale</div>
  <div class="social"><span></span><span></span><span></span><span></span><span></span><span></span></div>
  <nav class="footer-nav"><span class="active">About</span><span>Team</span><span>Listings</span><span>Contact</span></nav>
</footer>
<div class="copyright">Copyright © 2023 Kestrel Vale Business Brokers - All Rights Reserved.</div>

</body>
</html>
```